Elevated, strategic rebranding needed! Larkfield Terrace Brochure

This is a rebranding project and we need flyers to use for marketing materials to physicians, case managers, families, and hospitals. Tamarind Unified Wellness just acquired this massive, gorgeous campus and we need to rebrand now! The public has known this as Meridian Holloway Grove since 2008. It has been stuck in its ways (albeit it has had a strong reputation) for years. We are bringing them into the new world of senior care! Larkfield Terrace is redefining senior care in Fernhollow, Oklahoma. As part of Tamarind Unified Wellness, we're breaking away from the community's legacy as a traditional Catholic nonprofit to become an exciting, energetic, and extraordinary campus where exceptional care meets genuine innovation. We offer a full continuum of living options—independent living, assisted living, memory care, skilled nursing, and long-term care—with an integrated approach that addresses every aspect of our residents' lives: mental, physical, spiritual, and psychosocial wellness. Through strategic partnerships with best-in-class ancillary providers and our holistic care philosophy, we deliver coordinated, comprehensive care that honors aging adults and empowers them at every level. We are creating a community where remarkable outcomes happen every day. We need marketing materials that capture this energy, sophistication, and forward-thinking approach as we introduce Fernhollow to the new Larkfield Terrace. Our website is just a splash page at www.larkfieldterrace-example.com and our parent company is Tamarind Unified Wellness. www.tamarinduw-example.com
We want Larkfield to stand alone but wanted you to read about our vision and mission at Tamarind.

Target Market(s)

Senior Healthcare, hospitals, physicians, families

Industry/Entity Type

Healthcare

Requirements
Must have
• multicultural representation, emphasis on quality and purpose for seniors; every level of care; stunning campus; friendships, community, culture, health
Nice to have
• pictures that are not on every person's websites, pictures of different levels of health but still dignified,
Should not have
• should not make aging adults appear helpless, frail, and sad.

```html
<!DOCTYPE html>
<html lang="en">
<head>
<meta charset="utf-8">
<title>Larkfield Terrace – Welcome Home Flyer</title>
<link href="https://fonts.googleapis.com/css2?family=Montserrat:ital,wght@0,300;0,400;0,500;0,600;0,700;1,500&display=swap" rel="stylesheet">
<style>
  :root{
    --stage:#d9d9d9;
    --paper:#ffffff;
    --ink:#141414;
    --gold:#d6ad55;
    --gold-soft:#e8c98a;
    --amber:#e4a366;
    --amber-deep:#d38f4e;
    --brown-ink:#2a1a0c;
  }
  *{margin:0;padding:0;box-sizing:border-box;}
  html,body{width:1200px;height:849px;overflow:hidden;}
  body{background:var(--stage);font-family:"Montserrat",sans-serif;color:var(--ink);position:relative;}
  .flyer{position:absolute;left:317px;top:24px;width:565px;height:800px;background:var(--paper);overflow:hidden;}
  .abs{position:absolute;}

  .hero-photo{left:0;top:0;width:565px;height:340px;
    background:linear-gradient(160deg,#2a3329 0%,#3a3a36 35%,#4a4038 60%,#2c3038 100%);}
  .hero-shade{left:0;top:0;width:565px;height:340px;background:rgba(20,22,26,.45);}
  .hero-curve{left:0;top:0;width:565px;height:340px;}

  .brand-name{left:0;width:565px;top:150px;text-align:center;color:var(--gold);
    font-weight:400;font-size:17px;letter-spacing:5px;padding-left:10px;white-space:nowrap;}

  .circle-photo{left:44px;top:200px;width:192px;height:192px;border-radius:50%;
    background:radial-gradient(circle at 45% 40%,#c9a98a 0%,#8a8f9c 45%,#5a6a8a 75%,#d7d0c6 100%);
    box-shadow:0 6px 14px rgba(0,0,0,.25);}

  .welcome{left:269px;top:245px;font-style:italic;font-weight:500;font-size:50px;line-height:44px;letter-spacing:.5px;white-space:nowrap;}
  .intro{left:272px;top:347px;font-size:11.8px;line-height:14.2px;font-weight:400;white-space:nowrap;}

  .mist-band{left:0;top:455px;width:565px;height:260px;
    background:linear-gradient(180deg,#fafafa 0%,#f1f1f1 60%,#e4e4e4 85%,#f5f5f5 100%);}

  .choices-title{left:56px;top:418px;font-size:16.6px;line-height:19.7px;font-weight:600;white-space:nowrap;}
  .gold-rule{left:56px;top:489px;width:220px;height:2px;background:var(--gold);}
  .dot-arc{left:30px;top:460px;width:20px;height:62px;}

  .care-grid{left:62px;top:521px;width:200px;}
  .care-item{position:absolute;width:57px;text-align:center;}
  .care-box{width:57px;height:47px;border:1.4px solid var(--gold-soft);border-radius:4px;background:#fff;display:flex;align-items:center;justify-content:center;}
  .care-box svg{width:36px;height:36px;}
  .care-label{margin-top:6px;font-size:8.4px;line-height:9.2px;color:#222;white-space:nowrap;}

  .dance-photo{left:309px;top:447px;width:220px;height:214px;border-radius:26px 26px 0 26px;
    background:linear-gradient(120deg,#e9ecee 0%,#dfe4e6 40%,#d8c36b 55%,#d9dde0 70%,#3e6a8a 90%);}

  .contact-panel{left:0;top:701px;width:230px;height:99px;background:#000;}
  .contact-cta{left:67px;top:727px;color:#fff;font-size:13.5px;line-height:16px;font-weight:500;white-space:nowrap;}
  .contact-cta strong{font-weight:700;}

  .info-band{left:230px;top:717px;width:335px;height:83px;
    background:linear-gradient(100deg,var(--amber) 0%,var(--amber-deep) 55%,var(--amber) 100%);}
  .info-lines{left:245px;top:733px;font-size:12.2px;line-height:16px;font-weight:500;color:var(--brown-ink);white-space:nowrap;}
  .info-divider{left:420px;top:725px;width:1.2px;height:63px;background:#3a2a1a;}
  .address{left:433px;top:737px;font-size:11px;line-height:13px;color:var(--brown-ink);white-space:nowrap;}
</style>
</head>
<body>
<main class="flyer">
  <div class="abs hero-photo" role="img" aria-label="Photo of smiling multicultural seniors laughing together outdoors"></div>
  <div class="abs hero-shade"></div>
  <svg class="abs hero-curve" viewBox="0 0 565 340" preserveAspectRatio="none" aria-hidden="true">
    <path d="M0 340 L0 337 C70 300 140 275 230 245 C320 218 430 200 565 218 L565 340 Z" fill="var(--paper)"/>
    <path d="M470 208 C510 207 540 210 565 216" stroke="#e6ebef" stroke-width="3" fill="none"/>
  </svg>

  <div class="abs brand-name">LARKFIELD TERRACE</div>

  <div class="abs circle-photo" role="img" aria-label="Photo of seniors playing a block-stacking game at a table"></div>

  <h1 class="abs welcome">Welcome<br>Home.</h1>
  <p class="abs intro">Larkfield Terrace is an active<br>retirement community in Fernhollow<br>with independent, assisted, skilled<br>nursing and rehabilitation care options.</p>

  <div class="abs mist-band" role="img" aria-label="Soft faded photo of joined hands"></div>

  <h2 class="abs choices-title">Living Choices with<br>Differing Levels<br>of Care to Suit Your Needs.</h2>
  <svg class="abs dot-arc" viewBox="0 0 20 62" aria-hidden="true">
    <path d="M16 2 C2 20 2 42 16 60" stroke="#999" stroke-width="1.2" stroke-dasharray="1.5 3" fill="none"/>
  </svg>
  <div class="abs gold-rule"></div>

  <section class="abs care-grid">
    <div class="care-item" style="left:0;top:0">
      <div class="care-box"><svg viewBox="0 0 36 36" fill="none" stroke="var(--gold)" stroke-width="1.6" stroke-linejoin="round"><path d="M5 17 L18 5 L31 17"/><path d="M9 14 V31 H27 V14"/><rect x="15" y="18" width="7" height="5" rx="1"/></svg></div>
      <div class="care-label">Independent<br>Living</div>
    </div>
    <div class="care-item" style="left:69px;top:0">
      <div class="care-box"><svg viewBox="0 0 36 36" fill="none" stroke="var(--gold)" stroke-width="1.6" stroke-linecap="round" stroke-linejoin="round"><rect x="2" y="13" width="4" height="11"/><rect x="30" y="13" width="4" height="11"/><path d="M6 15 L12 12 L18 14 L23 11 L30 14"/><path d="M6 22 L10 24 L14 20 L18 24 L22 20 L26 23 L30 21"/><path d="M14 16 L18 19"/></svg></div>
      <div class="care-label">Assisted<br>Living</div>
    </div>
    <div class="care-item" style="left:138px;top:0">
      <div class="care-box"><svg viewBox="0 0 36 36" fill="none" stroke="var(--gold)" stroke-width="1.6" stroke-linecap="round"><path d="M18 5 C12 5 7 9 7 15 C4 17 5 23 9 24 C10 29 15 31 18 29 C21 31 26 29 27 24 C31 23 32 17 29 15 C29 9 24 5 18 5 Z"/><path d="M18 5 V29"/><circle cx="13" cy="14" r="1.5"/><circle cx="23" cy="20" r="1.5"/><path d="M13 16 V22 H18 M23 18 V12 H18"/></svg></div>
      <div class="care-label">Memory<br>Care</div>
    </div>
    <div class="care-item" style="left:0;top:79px">
      <div class="care-box"><svg viewBox="0 0 36 36" fill="none" stroke="var(--gold)" stroke-width="1.6" stroke-linecap="round"><circle cx="18" cy="10" r="6"/><path d="M6 32 C6 23 11 19 18 19 C25 19 30 23 30 32 Z"/><circle cx="13" cy="27" r="2"/><path d="M13 25 V20 M23 20 V25 M21 27 V25 H25 V27"/></svg></div>
      <div class="care-label">Skilled<br>Nursing</div>
    </div>
    <div class="care-item" style="left:69px;top:79px">
      <div class="care-box"><svg viewBox="0 0 36 36" fill="none" stroke="var(--gold)" stroke-width="1.6" stroke-linecap="round" stroke-linejoin="round"><path d="M18 17 C12 12 12 6 15 6 C17 6 18 8 18 9 C18 8 19 6 21 6 C24 6 24 12 18 17 Z"/><path d="M5 26 H12 L18 28 L31 23 C32 22 31 20 29 21 L22 23 H15"/><path d="M5 22 H12 L17 23"/></svg></div>
      <div class="care-label">Long-Term<br>Care</div>
    </div>
  </section>

  <div class="abs dance-photo" role="img" aria-label="Photo of three joyful seniors dancing together in a bright room"></div>

  <div class="abs contact-panel"></div>
  <p class="abs contact-cta"><strong>CONTACT US</strong><br>AND<br>SCHEDULE A TOUR!</p>

  <div class="abs info-band"></div>
  <p class="abs info-lines">(555) 014-2270<br>info@larkfieldterrace.com<br>larkfieldterrace.com</p>
  <div class="abs info-divider"></div>
  <p class="abs address">Larkfield Terrace<br>2750 Meadowlark Lane<br>Fernhollow, OK 74010</p>
</main>
</body>
</html>
```